Flyer Design Project for Sports Medicine Services

I am a sports medicine doctor specialising in the diagnosis and management of sport and exercise injuries for all ages and levels of activity - from elite to weekend jogger. I work under the Business name Peak Motion Athletic Care and do have a company logo. I am wanting a flier that I can send to family doctors, physiotherapists and sports clubs explaining who I am what I can offer and why they should send me patients.
- I have a Masters in Sports Medicine (MSportsMed), Diplomas in Obstetrics/Gynaecology (DRANZCOG) and also Paediatrics (DCH) and certificate in advanced clinical hypnosis
-accurate diagnosis and management plan with their regular physio to return the player / athlete to the field / court /gym as soon as safely possible
-hypnosis for sports performance eg anxiety control, confidence and mental rehearsal for individuals and teams
- because there are many possible therapists and therapy options, as a sports doctor I can work out who they need to see a physiotherapist, surgeon, massage therapist chiropractor or podiatrist to return them to activity or whether cortisone, PRP or autologous blood injections are needed
-can provide one point of contact for coaches and clubs for rehabilitation and return to sport advice.
- work with Clara Hutchings ex Australian Athlete, a Performance Strategist (NRC listed resource person) and registered Psychologist for best mental preparation for individuals teams and coach development
- can organise rapid access to MRI, ultrasound and specialist appointments if needed
-I work at 3 practices KineCore 418 Tolley Rd Marion 84619032 Monday Wednesday Friday; Harrow Lane Sports Clinic, 153 Denholm Rd, Adelaide 81764290 Tuesday Riverbend Falcons Sports Medicine Clinic, Norvale Park 8291 6475 Thursday.
-facebook site peakmotionathleticcare
Updates
Hi All, just to clarify.. My name is Paul Denton and I am the sports doctor. My wife is Clara Hutchings and she is the psychologist. The flier should mainly be advertising my sports medicine services and a byline ( or at least not the first line in the title) about the Performance Strategy and Coach development.
Target Market(s)
family doctors (GPs), Sporting Clubs, Physiotherapists
Industry/Entity Type
Massage
Look and feel

```html
<!DOCTYPE html>
<html lang="en">
<head>
<meta charset="utf-8">
<title>Peak Motion Athletic Care – Sports Medicine Flyer</title>
<link href="https://fonts.googleapis.com/css2?family=Arimo:wght@700&family=Roboto+Condensed:wght@300;400&family=Noto+Sans:wght@400&family=Mulish:wght@400;700&display=swap" rel="stylesheet">
<style>
  :root {
    --ink: #000000;
    --sky: #29a8e0;
    --lime: #a6ce39;
    --white: #ffffff;
    --footer-ink: #1b1b1b;
    --scan-deep: #0a1a3c;
    --scan-mid: #1f5fb4;
    --scan-glow: #5a3a8f;
  }
  * { box-sizing: border-box; margin: 0; padding: 0; }
  html, body { width: 847px; height: 1200px; overflow: hidden; background: var(--ink); }
  .flyer { position: relative; width: 847px; height: 1200px; background: var(--ink); color: var(--white); }

  .brand { position: absolute; left: 60px; top: 130px; display: flex; flex-direction: column; align-items: center; }
  .brand-dot { width: 96px; height: 96px; border-radius: 50%; background: var(--sky); margin-bottom: 28px; }
  .brand-name { font-family: "Mulish", sans-serif; font-weight: 700; color: var(--sky); font-size: 38px; line-height: 42px; text-align: center; letter-spacing: -0.5px; }

  .spine-scan { position: absolute; left: 421px; top: 0; width: 426px; height: 401px;
    background: radial-gradient(ellipse 90px 120px at 52% 72%, var(--scan-glow), transparent 70%),
                radial-gradient(ellipse 220px 260px at 50% 45%, var(--scan-mid), var(--scan-deep) 80%); }

  .service-band { position: absolute; left: 0; top: 401px; width: 847px; height: 150px; background: var(--sky); }
  .service-title { position: absolute; left: 294px; top: 412px; font-family: "Arimo", sans-serif; font-weight: 700; font-size: 31px; line-height: 42px; color: var(--white); }

  .doctor-portrait { position: absolute; left: 64px; top: 364px; width: 211px; height: 225px; border: 3px solid var(--white); border-radius: 18px; background: var(--lime); }

  .intro { position: absolute; left: 48px; top: 622px; width: 760px; font-family: "Roboto Condensed", sans-serif; font-weight: 400; font-size: 27px; line-height: 36px; }

  .credentials { position: absolute; left: 48px; top: 766px; width: 770px; list-style: none; font-family: "Noto Sans", sans-serif; font-size: 16.5px; line-height: 25px; }
  .credentials li { position: relative; padding-left: 28px; margin-bottom: 24px; text-align: justify; }
  .credentials li::before { content: ""; position: absolute; left: 2px; top: 7px; width: 12px; height: 12px; border-radius: 50%; background: var(--lime); }

  .locations { position: absolute; left: 0; top: 1079px; width: 847px; height: 121px; background: var(--lime); display: flex; padding: 18px 0 0 40px; font-family: "Mulish", sans-serif; color: var(--footer-ink); }
  .location { padding-right: 18px; }
  .location + .location { border-left: 1.5px solid var(--white); padding-left: 18px; height: 82px; }
  .location-day { font-size: 14px; line-height: 20px; }
  .location-name { font-weight: 700; font-size: 16.5px; line-height: 22px; }
  .location-address { font-size: 14.5px; line-height: 19px; }
  .location-phone { font-weight: 700; font-size: 15.5px; line-height: 21px; }
  .loc-marion { width: 237px; }
  .loc-harrow { width: 238px; }
  .loc-riverbend { flex: 1; }
</style>
</head>
<body>
<main class="flyer">
  <header class="brand">
    <span class="brand-dot" aria-hidden="true"></span>
    <h1 class="brand-name">Peak Motion<br>Athletic Care</h1>
  </header>

  <div class="spine-scan" role="img" aria-label="Blue x-ray style illustration of a human torso and spine with a red glow at the lower back"></div>

  <div class="service-band"></div>
  <div class="doctor-portrait" role="img" aria-label="Portrait photograph of Dr Paul Denton"></div>
  <h2 class="service-title">Sport Injuries Diagnosis<br>and Treatment<br>High Performance Psychology</h2>

  <p class="intro">Paul Denton a Sports Medicine &amp; Exercise Injuries Doctor specialising in the diagnosis and management of sport and exercise injuries for all ages and levels of activity - from elite to weekend jogger.</p>

  <ul class="credentials">
    <li>Paul has a Masters in Sports Medicine (MSportsMed), Diplomas in Obstetrics /Gynaecology (DRANZCOG) and also Paediatrics (DCH) and certificate in advanced clinical hypnosis</li>
    <li>Accurate diagnosis and management plan with their regular physio to return the player / athlete to the field / court /gym as soon as safely possible</li>
    <li>Hypnosis for sports performance eg anxiety control, confidence and mental rehearsal for individuals and teams</li>
    <li>Rapid access to specialists if needed. Rapid referrals for MRI ultrasound and xrays</li>
  </ul>

  <footer class="locations">
    <div class="location loc-marion">
      <p class="location-day">Monday, Wednesday, Friday</p>
      <p class="location-name">KineCore</p>
      <p class="location-address">418 Tolley Rd Marion</p>
      <p class="location-phone">84619032</p>
    </div>
    <div class="location loc-harrow">
      <p class="location-day">Tuesday</p>
      <p class="location-name">Harrow Lane Sports Clinic</p>
      <p class="location-address">153 Denholm Rd, Adelaide</p>
      <p class="location-phone">81764290</p>
    </div>
    <div class="location loc-riverbend">
      <p class="location-day">Thursday</p>
      <p class="location-name">Riverbend Falcons Sports Medicine Clinic</p>
      <p class="location-address">Norvale Park</p>
      <p class="location-phone">8291 6475</p>
    </div>
  </footer>
</main>
</body>
</html>
```